Business Card Design Project

use presentation folder design and my logo and make 4 over 4 business cards

Industry/Entity Type

Business

Requirements
Must have
• use the design from my presentation folder and put my logo on it

Name
Title
phone
fax
email

```html
<!DOCTYPE html>
<html lang="en">
<head>
<meta charset="utf-8">
<title>BrightPath Counseling – Business Cards</title>
<link rel="stylesheet" href="https://fonts.googleapis.com/css2?family=Didact+Gothic&family=Questrial&display=swap">
<style>
  :root {
    --backdrop: #4f4f51;
    --front-light: #dccdb2;
    --front-dark: #c6b393;
    --back-light: #7a6636;
    --back-dark: #5f4e27;
    --ink-dark: #2f2c28;
    --ink-light: #fbf8f2;
    --mark-faint: rgba(150, 124, 84, 0.28);
  }
  * { box-sizing: border-box; margin: 0; padding: 0; }
  html, body {
    width: 942px;
    height: 1200px;
    overflow: hidden;
    background: var(--backdrop);
    font-family: "Didact Gothic", sans-serif;
  }
  .sheet {
    position: relative;
    width: 942px;
    height: 1200px;
  }
  .card {
    position: absolute;
    left: 165px;
    width: 612px;
    height: 350px;
    box-shadow: 0 14px 30px rgba(0, 0, 0, 0.35);
    overflow: hidden;
  }
  .card--front {
    top: 135px;
    background: linear-gradient(135deg, var(--front-light), var(--front-dark));
  }
  .card--back {
    top: 725px;
    background: linear-gradient(135deg, var(--back-light), var(--back-dark));
  }

  /* front */
  .front-accent {
    position: absolute;
    left: -60px;
    top: 20px;
    width: 300px;
    height: 300px;
    border-radius: 50%;
    background: var(--mark-faint);
  }
  .identity {
    position: absolute;
    right: 34px;
    top: 26px;
    text-align: left;
    color: var(--ink-dark);
  }
  .identity__first {
    font-size: 30px;
    line-height: 1;
    margin-left: 34px;
  }
  .identity__last {
    font-size: 54px;
    line-height: 1;
    letter-spacing: -0.5px;
  }
  .identity__title {
    font-size: 19px;
    letter-spacing: 7px;
    margin-left: 20px;
    color: var(--ink-light);
  }
  .contact {
    position: absolute;
    left: 300px;
    top: 190px;
    font-size: 15px;
    color: var(--ink-light);
    border-collapse: collapse;
  }
  .contact td { padding: 4px 0; }
  .contact__label { width: 58px; color: var(--ink-dark); }

  /* back */
  .brand {
    position: absolute;
    left: 150px;
    top: 118px;
    color: var(--ink-light);
    font-family: "Questrial", sans-serif;
  }
  .brand__row {
    display: flex;
    align-items: center;
    gap: 14px;
  }
  .brand__dot {
    width: 44px;
    height: 44px;
    border-radius: 50%;
    background: var(--ink-light);
  }
  .brand__name { font-size: 34px; line-height: 1; }
  .brand__tagline {
    margin-top: 12px;
    margin-left: 4px;
    font-size: 18px;
    letter-spacing: 0.5px;
  }
</style>
</head>
<body>
<main class="sheet">
  <section class="card card--front" aria-label="Business card front">
    <div class="front-accent" aria-hidden="true"></div>
    <div class="identity">
      <p class="identity__first">Dorian</p>
      <p class="identity__last">Whitfield</p>
      <p class="identity__title">founder / CEO</p>
    </div>
    <table class="contact">
      <tr><td class="contact__label">phone</td><td>404.555.0182</td></tr>
      <tr><td class="contact__label">fax</td><td>678.555.0247</td></tr>
      <tr><td class="contact__label">email</td><td>BrightPathCare@mailbox.com</td></tr>
    </table>
  </section>

  <section class="card card--back" aria-label="Business card back">
    <div class="brand">
      <div class="brand__row">
        <span class="brand__dot" aria-hidden="true"></span>
        <span class="brand__name">BrightPath Counseling</span>
      </div>
      <p class="brand__tagline">a pro active addiction center</p>
    </div>
  </section>
</main>
</body>
</html>
```